Breezeway Comfort business cards design

Need a business card design for a Heating and Air Conditioning business. I need these items included.
Business name: Breezeway Comfort
Owner: Marcus Tollefsen
License # 2874590
Phone number # 555-382-4071
Email: breezewaycomfortair@mailvista.example
Sales
Service
Installation
Maintenance

Heating and Air Conditioning

Requirements
Must have
• Company name , license number , phone number , email

```html
<!DOCTYPE html>
<html lang="en">
<head>
<meta charset="utf-8">
<title>Breezeway Comfort – Business Cards</title>
<link rel="stylesheet" href="https://fonts.googleapis.com/css2?family=Montserrat:wght@400;600;700&display=swap">
<style>
  :root {
    --page-bg: #e9e9e9;
    --card-dark: #222222;
    --pattern-a: #262626;
    --pattern-b: #2f2f2f;
    --card-light: #ffffff;
    --brand-blue: #1f3f9a;
    --brand-orange: #f26b2e;
    --ink-gray: #666666;
    --rule-gray: #7a7a7a;
  }
  * { box-sizing: border-box; margin: 0; padding: 0; }
  html, body {
    width: 1200px; height: 1000px; overflow: hidden;
    background: var(--page-bg);
    font-family: "Montserrat", sans-serif;
  }
  .canvas { position: relative; width: 1200px; height: 1000px; }

  .card { position: absolute; width: 778px; height: 448px; left: 211px; }
  .card--front { top: 31px; background: var(--card-dark); overflow: hidden; }
  .card--back { top: 511px; background: var(--card-light); }

  .front__pattern {
    position: absolute; inset: 0;
    background: radial-gradient(circle at 20% 30%, var(--pattern-b), var(--pattern-a) 60%, var(--card-dark));
  }
  .front__brand {
    position: absolute; left: 420px; top: 287px;
    display: flex; align-items: center; gap: 14px;
  }
  .brand-dot {
    width: 54px; height: 54px; border-radius: 50%;
    background: var(--brand-orange);
  }
  .front__brand .brand-name {
    font-weight: 700; font-size: 30px; color: var(--brand-orange);
    letter-spacing: 0.5px;
  }

  .back__brand {
    position: absolute; left: 60px; top: 120px; width: 260px;
    display: flex; flex-direction: column; align-items: center; gap: 18px;
  }
  .back__brand .brand-dot { width: 110px; height: 110px; }
  .back__brand .brand-name {
    font-weight: 700; font-size: 32px; line-height: 1.1;
    color: var(--brand-blue); text-align: center;
  }
  .back__divider {
    position: absolute; left: 389px; top: 110px;
    width: 1px; height: 228px; background: var(--rule-gray);
  }
  .contact {
    position: absolute; left: 390px; width: 388px; top: 128px;
    text-align: center; color: var(--ink-gray);
  }
  .contact__name { font-weight: 700; font-size: 25px; color: var(--brand-blue); line-height: 1.2; }
  .contact__role { font-weight: 600; font-size: 24px; color: var(--brand-orange); line-height: 1.2; }
  .contact__icons { display: flex; justify-content: center; gap: 5px; margin-top: 12px; }
  .contact__icons svg { width: 28px; height: 28px; }
  .contact__phone { font-size: 18px; letter-spacing: 1.5px; margin-top: 4px; }
  .contact__email { font-size: 16px; margin-top: 2px; }
  .contact__license { font-size: 18px; margin-top: 20px; }

  .services {
    position: absolute; left: 0; right: 0; top: 408px;
    text-align: center; font-weight: 600; font-size: 13px;
    letter-spacing: 3.5px; color: var(--ink-gray);
  }
</style>
</head>
<body>
<main class="canvas">
  <section class="card card--front" aria-label="Card front">
    <div class="front__pattern" role="img" aria-label="Repeating tone-on-tone pattern of the company emblem"></div>
    <div class="front__brand">
      <span class="brand-dot" aria-hidden="true"></span>
      <span class="brand-name">Breezeway Comfort</span>
    </div>
  </section>

  <section class="card card--back" aria-label="Card back">
    <div class="back__brand">
      <span class="brand-dot" aria-hidden="true"></span>
      <span class="brand-name">Breezeway<br>Comfort</span>
    </div>
    <div class="back__divider"></div>
    <div class="contact">
      <p class="contact__name">Marcus Tollefsen</p>
      <p class="contact__role">Owner</p>
      <div class="contact__icons">
        <svg viewBox="0 0 28 28" aria-label="Phone">
          <circle cx="14" cy="14" r="12.5" fill="none" stroke="#1f3f9a" stroke-width="1.6"/>
          <path d="M10 8.5c1-.6 1.8-.4 2.3.6l.9 1.9c.3.7.1 1.3-.5 1.7l-.7.5c.6 1.6 1.6 2.8 3 3.6l.6-.6c.5-.5 1.1-.6 1.7-.2l1.8 1.1c.8.5.9 1.4.2 2.2-1 1.1-2.4 1.2-3.8.5-2.8-1.4-4.9-3.9-5.9-6.9-.5-1.6-.3-3.4.4-4.4z" fill="#1f3f9a"/>
        </svg>
        <svg viewBox="0 0 28 28" aria-label="Email">
          <circle cx="14" cy="14" r="12.5" fill="none" stroke="#1f3f9a" stroke-width="1.6"/>
          <rect x="7.5" y="9.5" width="13" height="9" rx="1" fill="#1f3f9a"/>
          <path d="M7.8 10l6.2 4.8 6.2-4.8M7.8 18.2l4.5-4M20.2 18.2l-4.5-4" fill="none" stroke="#ffffff" stroke-width="1"/>
        </svg>
      </div>
      <p class="contact__phone">555-382-4071</p>
      <p class="contact__email">breezewaycomfortair@mailvista.example</p>
      <p class="contact__license">License # 2874590</p>
    </div>
    <p class="services">SALES · SERVICE · INSTALLATION · MAINTENANCE</p>
  </section>
</main>
</body>
</html>
```